Corbel Crest Lighting - Commercial & Residential Landscape Lighting

Landscape Lighting Services & Design: Create a website for our landscape lighting company. We would like the design to be tailored around this description:
Illuminate with Confidence. Designed with Precision. Installed with Care.
Locally and veteran-owned, we take pride in transforming outdoor spaces through innovative lighting solutions tailored to your vision. From landscape and holiday lighting to permanent installations, our effortless process and expert design deliver breathtaking results and lasting curb appeal. Backed by a lifetime warranty and quarterly service options, our commitment to quality and customer satisfaction is unwavering. Try before you buy and experience your home in a whole new light with our complimentary demo kit — see the stunning effects before you decide.
- Also, add in this information as well; Outdoor Lighting not only beautifies spaces but also significantly enhances safety by illuminating your home or business. Beautifully lit entrances deter potential intruders, making your home a safer place for your loved ones. we also offer quarterly service plans to ensure lighting equipment continues to operate & illuminate effectively throughout the year. Also mention we provide free estimates and we are offering a 10% discount to military, veterans, and first responders.

Target Market(s)

Luxury market

Industry/Entity Type

Landscape Lighting - Residential & Commercial Lighting Services

Coding

Coded - Design and coding required

Number of Pages Required

2 page

Colors
00AB8E
00BBA5
67D7C9
C6EFE9
E9F9F6
59FF00
82FF00
B8FF75
E3FFCB
F4FFEA
FFC000
F8CF3A
FAE287
FDF2CF
FEFAEE

Requirements
Must have
• a lead generation button where people can submit their information for us to reach out to them and schedule their free estimate, homepage, about page, contact page, products and services page, user friendly, easy to navigate, and it also must be engaging and eye popping, as well as appealing to the luxury market. Please use colors; verdent green, dark green, ivory, and sunny yellow. Also, include an about page that references our story; Glen is retired Army and he opened a fitness studio in 2017 with his wife Rosalind. He has installed low voltage lighting in every home he lived in and for his friends and family over the years and decided to open his own business because he is passionate about beautifying outdoor landscapes and highlighting a properties full potential, not only in the day but at night as well all while providing safety and security for his clients. Having a deep respect for nature and landscaping, he wants to provide the same care and quality to each of his clients as he has in the fitness industry for decades. He believes small businesses are the back bone of America and he's excited to provide a service that is all to often neglected in the design of a home.
Nice to have
• I would like to have a clear intent and purpose, engaging web design, clear call to action, optimized for search engines, mobile friendy design, security measures, credibility indicators

```html
<!DOCTYPE html>
<html lang="en">
<head>
<meta charset="utf-8">
<title>Corbel Crest Lighting — Landscape Lighting</title>
<link href="https://fonts.googleapis.com/css2?family=Lexend:wght@400;600&family=Urbanist:wght@400;500&family=Manrope:wght@700&display=swap" rel="stylesheet">
<style>
  :root {
    --night-deep: #0b1a22;
    --night-mid: #13262b;
    --night-warm: #2b2a1e;
    --teal: #00ab8e;
    --teal-bright: #1fc3ad;
    --white: #ffffff;
    --ink: #0d1f1c;
  }
  * { box-sizing: border-box; margin: 0; padding: 0; }
  html, body { width: 1200px; height: 675px; overflow: hidden; background: var(--night-deep); }
  .hero {
    position: relative;
    width: 1200px;
    height: 675px;
    overflow: hidden;
    font-family: "Urbanist", sans-serif;
    color: var(--white);
  }
  .hero-photo {
    position: absolute; inset: 0;
    background:
      radial-gradient(ellipse 32% 22% at 50% 62%, rgba(214,160,70,0.38), transparent 70%),
      radial-gradient(ellipse 60% 40% at 55% 45%, rgba(70,80,70,0.35), transparent 75%),
      linear-gradient(180deg, #0f2230 0%, #17292c 35%, var(--night-warm) 62%, #1a2a22 78%, #0e2a27 86%, var(--teal-bright) 100%);
  }
  .hero-shade {
    position: absolute; left: 0; right: 0; top: 285px; height: 290px;
    background: rgba(4, 40, 40, 0.38);
  }
  .site-header {
    position: absolute; top: 28px; left: 80px; right: 48px;
    display: flex; align-items: center; justify-content: space-between;
  }
  .brand {
    font-family: "Urbanist", sans-serif; font-weight: 500; font-size: 20px;
    letter-spacing: 0.04em; color: var(--white);
  }
  .nav-group { display: flex; align-items: center; gap: 6px; }
  .main-nav {
    display: flex; gap: 22px; padding: 8px 20px;
    border: 1px solid rgba(255,255,255,0.75); border-radius: 999px;
    font-size: 11px; font-weight: 500;
  }
  .btn-estimate {
    background: var(--white); color: var(--ink);
    font-family: "Manrope", sans-serif; font-weight: 700; font-size: 11px;
    padding: 9px 22px; border-radius: 999px;
  }
  .hero-content {
    position: absolute; top: 262px; left: 0; right: 0; text-align: center;
  }
  .hero-title {
    font-family: "Lexend", sans-serif; font-weight: 600; font-size: 50px;
    line-height: 1.1; letter-spacing: 0.01em;
  }
  .hero-lead {
    margin: 26px auto 0; width: 620px;
    font-size: 23px; line-height: 1.05; font-weight: 400;
  }
  .hero-actions {
    margin-top: 40px; display: flex; justify-content: center; gap: 22px;
  }
  .btn {
    font-family: "Manrope", sans-serif; font-weight: 700; font-size: 15px;
    width: 188px; padding: 14px 0; border-radius: 999px; text-align: center;
  }
  .btn-primary { background: var(--teal); color: var(--white); }
  .btn-secondary { background: var(--white); color: var(--ink); }
</style>
</head>
<body>
  <section class="hero">
    <div class="hero-photo" role="img" aria-label="Two-storey brick home at night with warm landscape lighting among tall trees"></div>
    <div class="hero-shade"></div>
    <header class="site-header">
      <div class="brand">Corbel Crest Lighting</div>
      <div class="nav-group">
        <nav class="main-nav">
          <span>Home</span><span>About</span><span>Services</span><span>Our Work</span><span>Contact</span>
        </nav>
        <span class="btn-estimate">Free Estimate</span>
      </div>
    </header>
    <div class="hero-content">
      <h1 class="hero-title">Illuminate Your World with<br>Signature Precision.</h1>
      <p class="hero-lead">Luxury landscape lighting that blends design, safety, and timeless beauty.</p>
      <div class="hero-actions">
        <span class="btn btn-primary">Request Free Estimate</span>
        <span class="btn btn-secondary">Try Our Demo Kit</span>
      </div>
    </div>
  </section>
</body>
</html>
```